Silent Auction Design Piece (11x14, Full Color)

I am needing to build a new Silent auction piece. This one will be for Sport Courts. (Pickleball, Tennis, and Basketball) I will attach pics and a narrative). I would like to maintain the Black and Gold Theme but possibly change the lettering and motif to show more youth, fun and excitement around sports. Also remove pictures of my face and credentials. Use credentials but say it is from our professional team of designers.
Target Market(s)
Fundraising Gala Events (High Net Worth Customers)
Industry/Entity Type
Design & Architecture
Requirements
Must have
- Black and Gold Colors, Images oof Sport Courts, Narrative (see attached, Choose 1 of 5))
Nice to have
- Easy to read, make this piece exciting & attractive. We are selling to high end consumers!
Should not have
- Poor lettering, only bespoke fonts.

```html
<!DOCTYPE html>
<html lang="en">
<head>
<meta charset="utf-8">
<title>Silent Auction: Sport Court Design Package</title>
<link href="https://fonts.googleapis.com/css2?family=Oswald:wght@400;600;700&family=Arimo:ital,wght@0,400;0,700;1,400&display=swap" rel="stylesheet">
<style>
  :root {
    --stage: #d9d9d9;
    --black: #000000;
    --gold: #c2a53c;
    --gold-deep: #b39a3a;
    --white: #ffffff;
    --rule: #8c7a33;
    --rule-soft: #6b6b6b;
  }
  * { margin: 0; padding: 0; box-sizing: border-box; }
  html, body {
    width: 1200px; height: 2386px; overflow: hidden;
    background: var(--stage);
    font-family: "Arimo", Arial, sans-serif;
    color: var(--white);
  }
  .sheet {
    position: absolute; left: 171px; width: 858px;
    background: var(--black); overflow: hidden;
  }
  .sheet--front { top: 68px; height: 1091px; }
  .sheet--back { top: 1212px; height: 1092px; }
  .photo { position: absolute; left: 0; width: 858px; display: block; }
  .photo--hero { top: 0; height: 265px; }
  .photo--court { top: 766px; height: 326px; }
  .court-lines { position: absolute; pointer-events: none; }
  .block { position: absolute; left: 61px; width: 737px; font-size: 16px; line-height: 19.5px; }
  .centered { left: 0; width: 858px; text-align: center; }
  .title {
    font-family: "Oswald", "Arial Narrow", sans-serif;
    font-size: 46px; line-height: 52px; font-weight: 700;
    text-transform: uppercase; letter-spacing: 1px; color: var(--gold);
  }
  .subtitle {
    font-family: "Oswald", "Arial Narrow", sans-serif;
    font-size: 28px; line-height: 34px; font-weight: 400;
    text-transform: uppercase; letter-spacing: 2px;
  }
  .package-title {
    font-family: "Oswald", "Arial Narrow", sans-serif;
    font-size: 34px; line-height: 40px; font-weight: 600;
    text-transform: uppercase; letter-spacing: 1.5px;
  }
  .package-title .accent { color: var(--gold); }
  .rule { position: absolute; left: 79px; width: 701px; height: 2px; background: var(--rule); }
  .rule--soft { background: var(--rule-soft); height: 1px; }
  .offer-heading { font-weight: 700; }
  .tagline { font-style: italic; color: var(--gold); }
  .feature { left: 135px; width: 672px; }
  .feature::before {
    content: ""; position: absolute; left: -26px; top: 6px;
    width: 8px; height: 8px; border-radius: 50%; background: var(--gold);
  }
  .bid-details { font-weight: 700; }
  .bid-call {
    font-family: "Oswald", "Arial Narrow", sans-serif;
    font-size: 20px; line-height: 24px; font-weight: 600;
    text-transform: uppercase; letter-spacing: 1px; color: var(--gold);
  }
  .contact { color: var(--gold); font-style: italic; }
  .gold-bar { position: absolute; left: 74px; width: 710px; top: 1072px; height: 19px; background: var(--gold-deep); }
  .hero-stripe { position: absolute; left: 0; top: 265px; width: 858px; height: 4px; background: var(--gold); }
</style>
</head>
<body>

<section class="sheet sheet--front">
  <svg class="photo photo--hero" viewBox="0 0 858 265" role="img" aria-label="Two photos of a backyard basketball court with blue and yellow surface beside a modern white home">
    <defs>
      <linearGradient id="heroLeft" x1="0" y1="0" x2="0" y2="1">
        <stop offset="0" stop-color="#8fb0c8"/>
        <stop offset="0.45" stop-color="#9a8a6a"/>
        <stop offset="0.7" stop-color="#3d4fa8"/>
        <stop offset="1" stop-color="#2c3f9a"/>
      </linearGradient>
      <linearGradient id="heroRight" x1="0" y1="0" x2="0" y2="1">
        <stop offset="0" stop-color="#9cc0dc"/>
        <stop offset="0.5" stop-color="#c9c3b6"/>
        <stop offset="0.75" stop-color="#4a9a3a"/>
        <stop offset="1" stop-color="#2f47a8"/>
      </linearGradient>
    </defs>
    <polygon points="0,0 480,0 370,265 0,265" fill="url(#heroLeft)"/>
    <polygon points="493,0 858,0 858,265 383,265" fill="url(#heroRight)"/>
    <polygon points="480,0 493,0 383,265 370,265" fill="#ffffff"/>
  </svg>
  <div class="hero-stripe"></div>

  <svg class="court-lines" style="left:0;top:269px" width="858" height="140" viewBox="0 0 858 140" aria-hidden="true">
    <g fill="none" stroke="#c2a53c" stroke-opacity="0.22" stroke-width="2">
      <path d="M0,20 A90,90 0 0 1 90,110"/>
      <path d="M858,20 A90,90 0 0 0 768,110"/>
    </g>
  </svg>

  <h1 class="block centered title" style="top:290px">Non-Profit Piece for Sport Courts</h1>
  <p class="block centered subtitle" style="top:352px">Tech-Focused Innovation</p>
  <div class="rule" style="top:412px"></div>

  <h2 class="block offer-heading" style="top:440px">Exclusive Tech-Advanced Sport Court Design Experience</h2>
  <p class="block tagline" style="top:479px">Revolutionize Your Outdoor Space with State-of-the-Art Innovation</p>
  <p class="block" style="top:517px">Elevate your home with a custom sport court powered by cutting-edge technology from Vela Courtworks. As a dedicated supporter of [Non-Profit Organization/Gala Name], we proudly donate this premium package:</p>

  <p class="block feature" style="top:596px"><strong>Expert Consultation &amp; Innovative Design:</strong> Collaborate with our specialists to design a high-tech sport court (basketball, tennis, pickleball, or multi-sport) featuring smart LED systems, automated surfaces, and app integration, paired with elegant landscaping.</p>
  <p class="block feature" style="top:674px"><strong>Premium Inclusions:</strong> On-site evaluation, 3D visualizations, tech specs, and a blueprint redeemable toward installation.</p>
  <p class="block feature" style="top:732px"><strong>Tailored to You:</strong> Adaptable for any luxury residence, blending performance with aesthetic appeal.</p>

  <p class="block" style="top:810px">Valued at <strong>$2,500</strong>, this package showcases Vela Courtworks' commitment to futuristic athletic solutions. Redeem within 12 months</p>

  <div class="block centered bid-details" style="top:878px">
    <span class="bid-call">Bid Today to Unlock the Future of Home Sports!</span><br>
    Retail Value: $2,500<br>
    Minimum Bid: $199<br>
    Bid Increments: $50<br>
    Donated By: Vela Courtworks
  </div>

  <div class="block centered" style="top:1001px">
    <span class="contact">info@velacourtworks.com | www.velacourtworks.com</span><br>
    Non-transferable. No cash value. Subject to availability and terms.
  </div>

  <div class="gold-bar"></div>
</section>

<section class="sheet sheet--back">
  <svg class="court-lines" style="left:0;top:0" width="858" height="130" viewBox="0 0 858 130" aria-hidden="true">
    <g fill="none" stroke="#c2a53c" stroke-opacity="0.22" stroke-width="2">
      <path d="M0,10 A90,90 0 0 1 90,100"/>
      <path d="M858,10 A90,90 0 0 0 768,100"/>
    </g>
  </svg>

  <h1 class="block centered package-title" style="top:46px"><span class="accent">Luxury</span> Lifestyle Emphasis</h1>
  <div class="rule rule--soft" style="top:106px"></div>

  <h2 class="block offer-heading" style="top:140px">Bespoke Luxury Sport Court &amp; Landscaping Design</h2>
  <p class="block tagline" style="top:179px">Craft an Exquisite Private Retreat in Your Own Backyard</p>
  <p class="block" style="top:218px">Indulge in the sophistication of a personalized sport court from Vela Courtworks, where elegance meets innovation. In support of [Non-Profit Organization/Gala Name], we offer this exclusive opportunity:</p>

  <p class="block feature" style="top:276px"><strong>Personalized Design Consultation:</strong> Partner with our elite team for a custom sport court (tennis, basketball, or versatile options) enhanced by premium landscaping, incorporating high-end tech like ambient lighting and smart controls.</p>
  <p class="block feature" style="top:354px"><strong>Luxury Features:</strong> Detailed site analysis, high-fidelity renderings, material selections, and a comprehensive plan redeemable for your full project.</p>
  <p class="block feature" style="top:413px"><strong>Custom Elegance:</strong> Designed for discerning tastes, transforming any space into a refined athletic haven.</p>

  <p class="block" style="top:490px">This opulent package is valued at <strong>$2,500.</strong> Redeem within 12 months</p>

  <div class="block centered bid-details" style="top:541px">
    <span class="bid-call">Place Your Bid for Timeless Luxury!</span><br>
    Estimated Value: $2,500<br>
    Starting Bid: $199<br>
    Increments: $50<br>
    Courtesy of: Vela Courtworks
  </div>

  <div class="block centered" style="top:674px">
    <span class="contact">Contact: info@velacourtworks.com | www.velacourtworks.com</span><br>
    Non-transferable. No cash equivalent. Availability subject to scheduling.
  </div>

  <svg class="photo photo--court" viewBox="0 0 858 326" role="img" aria-label="Photo of a backyard half court with orange and blue surface beside a pool and dark modern house">
    <defs>
      <linearGradient id="courtScene" x1="0" y1="0" x2="0" y2="1">
        <stop offset="0" stop-color="#3a3a36"/>
        <stop offset="0.25" stop-color="#6f8a58"/>
        <stop offset="0.5" stop-color="#5b74b0"/>
        <stop offset="0.75" stop-color="#d8663e"/>
        <stop offset="1" stop-color="#c85a3a"/>
      </linearGradient>
    </defs>
    <rect width="858" height="326" fill="url(#courtScene)"/>
  </svg>
  <div class="hero-stripe" style="top:762px"></div>
</section>

</body>
</html>
```